Postcard and Door Hanger Design

We need two pieces designed for marketing. Both will use the same logo and photo just the text will be slightly different. We need these designs looking very modern, clean, and simple while having the important information to stand out.

Postcard: 2 sided
- Side 1 just have large logo with our website and phone number
- Side 2 below.
- 4 x 6
- Use photo of house provided
- "Going Above and Beyond Every Time"
- "Call TODAY to Reserve your project by May 1st and receive 10% off"
- "Residential and Commercial"
- Our contact is 778-294-1175
- Website is www.velmarcoatings.com
- Might include something like "check out our portfolio on our website"

Use the above as a guidline and be creative with it, add or take away as you see fit as we are open to suggestions.

Door Hanger: 2 sided
Side 1 - Logo with contact details
Side 2 - Below
- 4 x 11
- "We are painting your neighborhood"
-"come see us in action at (then leave a space where we can stick a label onto our door hanger with an address of a home we are painting)
- Call today for a FREE ESTIMATE
- 778-294-1175
- www.velmarcoatings.com

Links:

https://www.filenook.net/sh/q3k8tz52rwa9pn/TR7XKLP-QZ

https://www.filenook.net/sh/xv6rr27jtl3wyd/HNwLRaPqTs

Logo File:

https://www.filenook.net/sh/p2d94hzb1wkq07/zfa-R9LKiv

```html
<!DOCTYPE html>
<html lang="en">
<head>
<meta charset="utf-8">
<title>Velmar Coatings – Postcard Front</title>
<link rel="stylesheet" href="https://fonts.googleapis.com/css2?family=Marcellus&family=Roboto:wght@300;700&display=swap">
<style>
  :root {
    --paper: #ffffff;
    --slate: #414d57;
    --slate-deep: #343e47;
    --teal: #1fb8b4;
    --ink: #4a5763;
    --roller: #5b6772;
    --roller-fade: #eef0f2;
  }
  html, body {
    margin: 0;
    padding: 0;
    width: 1200px;
    height: 988px;
    overflow: hidden;
    background: var(--paper);
  }
  .postcard {
    position: relative;
    width: 1200px;
    height: 988px;
    background: var(--paper);
  }
  .paint-band {
    position: absolute;
    left: 0;
    top: 140px;
    width: 690px;
    height: 640px;
    background: linear-gradient(90deg, var(--slate) 0%, var(--slate) 70%, var(--slate-deep) 100%);
  }
  .roller-art {
    position: absolute;
    left: 679px;
    top: 55px;
    width: 521px;
    height: 765px;
    background: linear-gradient(90deg, var(--roller) 0%, var(--roller) 30%, #8a949d 48%, var(--roller-fade) 78%, var(--paper) 100%);
  }
  .brand-square {
    position: absolute;
    left: 320px;
    top: 320px;
    width: 72px;
    height: 72px;
    background: var(--teal);
  }
  .brand-name {
    position: absolute;
    left: 129px;
    top: 490px;
    margin: 0;
    font-family: "Marcellus", serif;
    font-weight: 400;
    font-size: 78px;
    line-height: 1;
    letter-spacing: 12px;
    color: var(--paper);
  }
  .brand-tagline {
    position: absolute;
    left: 131px;
    top: 578px;
    font-family: "Marcellus", serif;
    font-size: 34px;
    line-height: 1;
    letter-spacing: 33px;
    color: var(--paper);
  }
  .contact-phone {
    position: absolute;
    left: 92px;
    top: 830px;
    display: flex;
    align-items: center;
    gap: 18px;
    font-family: "Roboto", sans-serif;
    font-weight: 300;
    font-size: 64px;
    color: var(--teal);
    line-height: 1;
  }
  .contact-phone svg { width: 50px; height: 50px; }
  .contact-web {
    position: absolute;
    left: 141px;
    top: 904px;
    font-family: "Roboto", sans-serif;
    font-weight: 700;
    font-size: 40px;
    color: var(--ink);
    line-height: 1;
  }
</style>
</head>
<body>
<main class="postcard">
  <div class="paint-band"></div>

  <div class="roller-art" role="img" aria-label="Paint roller with handle rolling slate grey paint across the card"></div>

  <div class="brand-square"></div>
  <h1 class="brand-name">VELMAR</h1>
  <div class="brand-tagline">COATINGS</div>

  <div class="contact-phone">
    <svg viewBox="0 0 48 48" aria-hidden="true">
      <circle cx="24" cy="24" r="21" fill="none" stroke="var(--teal)" stroke-width="3"/>
      <path d="M18 13c-2 1-3 3-3 6 0 6 5 15 11 17 2 1 4 0 6-2l-4-5-3 1c-2-2-4-6-4-9l3-2-2-6z" fill="var(--teal)"/>
    </svg>
    <span>(778) 294-1175</span>
  </div>
  <div class="contact-web">www.velmarcoatings.com</div>
</main>
</body>
</html>
```